International Educational/Tuition/Learning Center

Company Background:
- Business card for a educational/tuition/learning center that provides supplementary lessons for students in Grade 7 to 12 ( Secondary and JC syllabus in the GCE 'O' and GCE 'A' level context but not limited to these. Future plans will be to cater for SAT, IB and HSCs programs.
- Name of company is called "THE QUILL AND LANTERN".
- Vision is to complement the basic principles of the rote learning culture and value-add by training the students to think out of the box and preserve creativity.
- To re-define and retain the value of the learning process.

Sketch Design:
- Simple and classy design that is mainly white-based with tinge of refreshing bright lime green.
- "New Age" simple and classy design that appeals to teenagers and young adults.
- Logo design to reinforce the vision of company.

Rough idea of what we have in mind but pls do not let this restrict your creativity:
- White and bright green base
- 2 sided print
- Front with simple information of Name and Designation as well as de-bossed/letterpressed print
- Details of on reverse side
- Contact details can be categorized as " find me" - address, "call me" - contact number , "email me" - email address, " Find out more"- website.

Information:

Name: Derek M Thalwin
Title: Managing Director
Address: 41 Kestrel Lane, #07-15, Singapore 654321
Contact: +65 93417260
Email: derekthalwin@mailvexo.com
Website: www.qnl-study.com

Thank you all in advance! Looking forward to some amazing designs from all you talented folks!
Updates

hi all,

have updated the projected to a guranteed status from the initial refundable status.

Thanks 

Dear designers,

I've included more info into the brief on design elements to include. 

Thanks for your participation and efforts!

Cheers!

Target Market(s)

young parents with school going children

Industry/Entity Type

Training

Requirements
Must have
• debossed/letterpressed logo
feel free to be creative with ur designs!
Nice to have
• round edges
Logo/name could have some elements of education/knowledge/path-to-learning incorporated in the design concept

```html
<!DOCTYPE html>
<html lang="en">
<head>
<meta charset="utf-8">
<title>The Quill and Lantern — Business Card</title>
<link rel="stylesheet" href="https://fonts.googleapis.com/css2?family=Tinos:wght@700&family=Questrial&display=swap">
<style>
  :root {
    --backdrop: #e6e6e4;
    --lime: #9ccc54;
    --lime-deep: #86bd3a;
    --ink: #111111;
    --card-black: #0b0b0b;
    --paper: #ffffff;
  }
  * { box-sizing: border-box; margin: 0; padding: 0; }
  html, body { width: 1067px; height: 1200px; overflow: hidden; }
  body {
    background: var(--backdrop);
    position: relative;
    font-family: "Questrial", sans-serif;
  }
  .card {
    position: absolute;
    left: 218px;
    width: 630px;
    height: 360px;
    border-radius: 6px;
    overflow: hidden;
    box-shadow: 0 14px 30px rgba(0,0,0,.22);
  }
  .card--front {
    top: 150px;
    background: linear-gradient(160deg, #a8d565 0%, var(--lime) 60%, var(--lime-deep) 100%);
    text-align: center;
  }
  .front__name {
    position: absolute;
    left: 0; right: 0; top: 140px;
    font-family: "Tinos", serif;
    font-weight: 700;
    font-size: 36px;
    color: var(--ink);
    letter-spacing: .5px;
  }
  .front__web {
    position: absolute;
    left: 0; right: 0; top: 232px;
    font-size: 13px;
    letter-spacing: 5px;
    color: var(--ink);
  }
  .card--back {
    top: 660px;
    background: var(--card-black);
    color: var(--paper);
  }
  .back__brand {
    position: absolute;
    left: 38px; top: 40px;
    font-family: "Tinos", serif;
    font-weight: 700;
    font-size: 20px;
    color: var(--paper);
  }
  .back__person {
    position: absolute;
    right: 60px; top: 52px;
    text-align: right;
  }
  .back__name { color: var(--lime); font-size: 20px; }
  .back__title { font-size: 13px; margin-top: 3px; }
  .back__details {
    position: absolute;
    left: 56px; top: 140px;
    font-size: 13px;
    line-height: 1.35;
  }
  .back__address { margin-bottom: 14px; }
  .back__label { color: var(--lime); display: inline-block; width: 20px; }
  .back__graphic {
    position: absolute;
    left: 140px; bottom: 0;
    width: 490px; height: 200px;
    background: linear-gradient(160deg, rgba(11,11,11,0) 0%, rgba(200,200,200,.35) 55%, rgba(156,204,84,.75) 100%);
  }
</style>
</head>
<body>
  <section class="card card--front">
    <h1 class="front__name">THE QUILL AND LANTERN</h1>
    <p class="front__web">www.qnl-study.com</p>
  </section>

  <section class="card card--back">
    <div class="back__graphic" role="img" aria-label="Decorative fan of white and lime green bars"></div>
    <div class="back__brand">THE QUILL AND LANTERN</div>
    <div class="back__person">
      <div class="back__name">Derek M Thalwin</div>
      <div class="back__title">Managing Director</div>
    </div>
    <div class="back__details">
      <p class="back__address">41 Kestrel Lane, #07-15,<br>Singapore 654321</p>
      <p><span class="back__label">P:</span>+65 93417260</p>
      <p><span class="back__label">E:</span>derekthalwin@mailvexo.com</p>
      <p><span class="back__label">W:</span>www.qnl-study.com</p>
    </div>
  </section>
</body>
</html>
```